Need Business Cards for my Business

email address: rkpmarlowhollowworks@vendrimail.com
web address: rkpmarlowhollowworks.net
Slogan: We offer various QVN licenses
Rowland K. Pemberly
Please stick with colors of Company Logo
would like the card to be more of the color example of the logo.
If you need PDF copy of logo email me at the above account.
Creative control rests with you.

Industry/Entity Type

Business

Contact Information for Business Card

I am a minimalist, but would like something to pop and stand out amongst other cards, make it memorable.

Font styles to use
Serif
Decorative
Script

```html
<!DOCTYPE html>
<html lang="en">
<head>
<meta charset="utf-8">
<title>Business Cards – Marlow Hollow Works</title>
<link href="https://fonts.googleapis.com/css2?family=Lato:wght@400;700&display=swap" rel="stylesheet">
<style>
  :root {
    --bg: #c6c6c6;
    --white: #ffffff;
    --blue-light: #2574b6;
    --blue-dark: #173d69;
    --red: #e52b2f;
    --ink: #1d1d1f;
  }
  html, body {
    margin: 0;
    padding: 0;
    width: 1197px;
    height: 1200px;
    overflow: hidden;
    background: var(--bg);
    font-family: "Lato", sans-serif;
  }
  .canvas { position: relative; width: 1197px; height: 1200px; }
  .card { position: absolute; border-radius: 5px; overflow: hidden; }

  .card-front {
    left: 263px; top: 171px; width: 673px; height: 383px;
    background: var(--white);
  }
  .brand {
    position: absolute; right: 40px; top: 62px;
    display: flex; align-items: center; gap: 12px;
  }
  .brand-mark { width: 22px; height: 22px; border-radius: 50%; background: var(--red); }
  .brand-name {
    font-weight: 700; font-size: 34px; letter-spacing: 1px;
    color: var(--blue-dark); text-transform: uppercase;
  }
  .person { position: absolute; left: 37px; top: 182px; }
  .person-name { margin: 0; font-weight: 700; font-size: 24px; color: var(--red); line-height: 1.1; }
  .person-title { margin: 2px 0 0; font-size: 16px; color: var(--ink); }

  .contact-band {
    position: absolute; left: 0; top: 252px; width: 100%; height: 83px;
    background: linear-gradient(180deg, var(--blue-light), var(--blue-dark));
  }
  .contact-list {
    list-style: none; margin: 0; padding: 8px 0 0 37px;
    color: var(--white); font-size: 18px; line-height: 22.5px;
  }
  .contact-list li { display: flex; align-items: center; gap: 8px; }
  .contact-list svg { width: 18px; height: 16px; fill: var(--red); flex: none; }
  .slogan {
    position: absolute; left: 37px; top: 346px; margin: 0;
    font-size: 18px; letter-spacing: 1px; color: var(--ink);
  }

  .card-back {
    left: 266px; top: 647px; width: 668px; height: 395px;
    background: linear-gradient(180deg, var(--blue-light), var(--blue-dark));
    display: flex; align-items: center; justify-content: center;
  }
  .card-back .brand { position: static; gap: 16px; }
  .card-back .brand-mark { width: 30px; height: 30px; }
  .card-back .brand-name { font-size: 42px; color: var(--white); }
</style>
</head>
<body>
<main class="canvas">
  <section class="card card-front">
    <div class="brand">
      <span class="brand-mark"></span>
      <span class="brand-name">Marlow Hollow Works</span>
    </div>
    <div class="person">
      <h1 class="person-name">Rowland K. Pemberly</h1>
      <p class="person-title">Managing Director</p>
    </div>
    <div class="contact-band">
      <ul class="contact-list">
        <li><svg viewBox="0 0 18 16"><path d="M1 5c0-3 4-4 8-4s8 1 8 4v1h-4V4.5C12 4 6 4 5 4.5V6H1z"/><path d="M4 8h10l2 7H2z"/></svg>555-014-2286</li>
        <li><svg viewBox="0 0 18 16"><path d="M1 2h16v12H1z M2.5 3.5 9 9l6.5-5.5" stroke="#fff" stroke-width="1"/></svg>rkpmarlowhollowworks@vendrimail.com</li>
        <li><svg viewBox="0 0 18 16"><circle cx="9" cy="8" r="7.5"/><path d="M1.5 8h15M9 .5v15M4 3.5h10M4 12.5h10" stroke="#fff" stroke-width="1" fill="none"/><ellipse cx="9" cy="8" rx="3.5" ry="7.5" stroke="#fff" stroke-width="1" fill="none"/></svg>www.rkpmarlowhollowworks.net</li>
      </ul>
    </div>
    <p class="slogan">We offer various QVN licenses</p>
  </section>

  <section class="card card-back">
    <div class="brand">
      <span class="brand-mark"></span>
      <span class="brand-name">Marlow Hollow Works</span>
    </div>
  </section>
</main>
</body>
</html>
```